Banner Design for High End Jewelry Website

We need a banner for our website (brindlestone.com) for a sale that we will be running. The banner should be a size 1187 × 400. I have included a few pieces of jewelry to be included in the banner (do not need to use all, can use just some). The banner should say:
"Christmas is Closer Than You Think Sale!"
Shop Now

Industry/Entity Type

Jewelry

```html
<!DOCTYPE html>
<html lang="en">
<head>
<meta charset="utf-8">
<title>Christmas Sale Banners</title>
<link rel="stylesheet" href="https://fonts.googleapis.com/css2?family=Cormorant+Garamond:wght@500;600;700&display=swap">
<style>
  :root {
    --page-top: #e9e9e9;
    --page-bottom: #f6f6f6;
    --sale-pink: #e6166b;
    --sky-blush: #ece0e4;
    --sky-mist: #dfe3ec;
    --sky-frost: #c9d4e2;
    --gold-soft: #dcb64a;
    --gold-muted: #c39a34;
    --ring-tone-a: #c9a94a;
    --ring-tone-b: #8e8a6a;
  }
  * { box-sizing: border-box; margin: 0; padding: 0; }
  html, body { width: 1200px; height: 826px; overflow: hidden; }
  body {
    position: relative;
    background: linear-gradient(180deg, var(--page-top) 0%, var(--page-bottom) 100%);
    font-family: "Cormorant Garamond", Georgia, serif;
  }
  .banner {
    position: absolute;
    left: 126px;
    width: 950px;
    height: 320px;
    overflow: hidden;
  }
  .banner--headline { top: 108px; }
  .banner--caps { top: 442px; }
  .winter-backdrop {
    position: absolute; inset: 0;
    background:
      radial-gradient(ellipse 60% 40% at 50% 0%, rgba(240,222,226,0.9), transparent 70%),
      radial-gradient(ellipse 40% 60% at 50% 80%, rgba(185,198,216,0.7), transparent 75%),
      linear-gradient(180deg, var(--sky-blush) 0%, var(--sky-mist) 45%, var(--sky-frost) 100%);
  }
  .product-photo {
    position: absolute;
    border-radius: 24px;
  }
  .product-photo--gold-band {
    background: linear-gradient(160deg, var(--gold-soft), var(--gold-muted));
  }
  .product-photo--cabochon-ring {
    background: linear-gradient(160deg, var(--ring-tone-a), var(--ring-tone-b));
  }
  .banner--headline .product-photo--gold-band { left: 36px; top: 84px; width: 170px; height: 164px; }
  .banner--headline .product-photo--cabochon-ring { left: 730px; top: 90px; width: 182px; height: 150px; }
  .banner--caps .product-photo--gold-band { left: 48px; top: 76px; width: 176px; height: 168px; }
  .banner--caps .product-photo--cabochon-ring { left: 714px; top: 83px; width: 189px; height: 155px; }

  .headline {
    position: absolute;
    left: 0; right: 18px;
    text-align: center;
    color: var(--sale-pink);
    font-weight: 600;
  }
  .headline--script {
    top: 110px;
    font-size: 52px;
    line-height: 52px;
    letter-spacing: 1.5px;
  }
  .headline--caps {
    top: 123px;
    right: 8px;
    font-size: 53px;
    line-height: 52px;
    letter-spacing: 0.5px;
    font-weight: 700;
  }
  .tagline {
    position: absolute;
    left: 0; right: 8px;
    top: 173px;
    text-align: center;
    color: var(--sale-pink);
    font-size: 28px;
    line-height: 34px;
    font-weight: 600;
    letter-spacing: 1.8px;
  }
</style>
</head>
<body>
  <section class="banner banner--headline">
    <div class="winter-backdrop" role="img" aria-label="Soft blurred winter forest with falling snow"></div>
    <div class="product-photo product-photo--gold-band" role="img" aria-label="Product photo: gold band ring with diamonds"></div>
    <h1 class="headline headline--script">Christmas is Closer<br>Than You Think Sale!</h1>
    <div class="product-photo product-photo--cabochon-ring" role="img" aria-label="Product photo: gold ring set with coloured gemstones"></div>
  </section>

  <section class="banner banner--caps">
    <div class="winter-backdrop" role="img" aria-label="Soft blurred winter forest with falling snow"></div>
    <div class="product-photo product-photo--gold-band" role="img" aria-label="Product photo: gold band ring with diamonds"></div>
    <h2 class="headline headline--caps">CHRISTMAS SALE</h2>
    <p class="tagline">It’s closer than you think.</p>
    <div class="product-photo product-photo--cabochon-ring" role="img" aria-label="Product photo: gold ring set with coloured gemstones"></div>
  </section>
</body>
</html>
```